Birch Harbor - Countertop fabricator
Need stationary, business card and T-shirt design
Birch Harbor - Countertop fabricator -
Creative Brief
Simple
Kevin Rasble
14 Larkwood Lane Syracuse, NY13099
info@birchharborny.example
www.birchharborny.example
Back of card to list materials; Granite Quatz Marble Soapstone Solid Surface

```html
<!DOCTYPE html>
<html lang="en">
<head>
<meta charset="utf-8">
<title>Birch Harbor Stationery</title>
<link href="https://fonts.googleapis.com/css2?family=Lato:wght@400;700&display=swap" rel="stylesheet">
<style>
  :root {
    --backdrop: #a7a9ab;
    --paper: #ffffff;
    --bronze: #8a6a35;
    --bronze-dark: #5e4520;
    --gold-light: #d8c49c;
    --ink: #2b2b2b;
    --window: #eeeeee;
  }
  html, body { margin: 0; padding: 0; overflow: hidden; }
  body {
    width: 1200px; height: 840px;
    background: var(--backdrop);
    font-family: "Lato", Arial, sans-serif;
    color: var(--ink);
    position: relative;
  }
  .piece {
    position: absolute;
    background: var(--paper);
    box-shadow: 0 2px 6px rgba(0,0,0,0.25);
    overflow: hidden;
  }
  .swoosh { position: absolute; top: 0; left: 0; width: 100%; }
  .brand {
    position: absolute;
    display: flex; flex-direction: column; align-items: center;
  }
  .brand-square { width: 30px; height: 30px; background: var(--bronze); }
  .brand-name {
    margin-top: 4px;
    font-weight: 700; color: var(--bronze-dark);
    letter-spacing: -0.2px; white-space: nowrap;
  }

  /* Envelope */
  .envelope { left: 72px; top: 240px; width: 564px; height: 259px; }
  .envelope .brand { left: 232px; top: 42px; }
  .envelope .brand-name { font-size: 15px; }
  .envelope-address {
    position: absolute; left: 22px; top: 122px;
    font-size: 8px; line-height: 11px;
  }
  .envelope-window {
    position: absolute; left: 307px; top: 144px; width: 185px; height: 84px;
    background: var(--window); border: 1px solid #d6d6d6; border-radius: 3px;
  }
  .envelope-url {
    position: absolute; right: 14px; bottom: 10px; font-size: 7px;
  }
  .bottom-band { position: absolute; left: 0; bottom: 0; width: 100%; height: 4px; background: var(--bronze); }

  /* Letterhead */
  .letterhead { left: 660px; top: 84px; width: 456px; height: 701px; }
  .letterhead .brand { left: 192px; top: 30px; }
  .letterhead .brand-name { font-size: 16px; }
  .letterhead-rule {
    position: absolute; left: 36px; right: 36px; top: 103px;
    height: 1px; background: var(--bronze);
  }
  .letterhead-footer {
    position: absolute; left: 0; right: 0; bottom: 12px;
    text-align: center; font-size: 7.5px; word-spacing: 1px;
  }

  /* Business card */
  .card { left: 245px; top: 547px; width: 223px; height: 149px; }
  .card .brand { left: 16px; top: 44px; }
  .card .brand-square { width: 24px; height: 24px; }
  .card .brand-name { font-size: 12px; }
  .card-panel {
    position: absolute; left: 110px; top: 0; width: 113px; height: 100%;
    background: var(--bronze); color: #f5eddd;
    padding: 10px 8px; box-sizing: border-box;
    font-size: 6px; line-height: 8px;
  }
  .card-name { font-size: 8px; font-weight: 700; }
  .card-role { margin-bottom: 14px; }
  .card-block { margin-bottom: 8px; }
</style>
</head>
<body>

<section class="piece envelope">
  <svg class="swoosh" viewBox="0 0 564 40" height="40" preserveAspectRatio="none" aria-hidden="true">
    <defs>
      <linearGradient id="envGrad" x1="0" x2="1">
        <stop offset="0" stop-color="#ffffff"/>
        <stop offset="0.5" stop-color="var(--gold-light)"/>
        <stop offset="1" stop-color="var(--bronze)"/>
      </linearGradient>
    </defs>
    <path d="M170 0 L564 0 L564 24 C460 10 320 6 170 0 Z" fill="url(#envGrad)"/>
  </svg>
  <div class="brand">
    <div class="brand-square"></div>
    <div class="brand-name">BirchHarbor</div>
  </div>
  <div class="envelope-address">
    14 Larkwood Lane<br>
    Syracuse, NY13099<br>
    P - 315-555-0142<br>
    F - 315-555-0178
  </div>
  <div class="envelope-window"></div>
  <div class="envelope-url">www.birchharborny.example</div>
  <div class="bottom-band"></div>
</section>

<section class="piece letterhead">
  <svg class="swoosh" viewBox="0 0 456 34" height="34" preserveAspectRatio="none" aria-hidden="true">
    <defs>
      <linearGradient id="lhGrad" x1="0" x2="1">
        <stop offset="0" stop-color="#ffffff"/>
        <stop offset="0.55" stop-color="var(--gold-light)"/>
        <stop offset="1" stop-color="var(--bronze)"/>
      </linearGradient>
    </defs>
    <path d="M110 0 L456 0 L456 22 C360 10 240 4 110 0 Z" fill="url(#lhGrad)"/>
  </svg>
  <div class="brand">
    <div class="brand-square"></div>
    <div class="brand-name">BirchHarbor</div>
  </div>
  <div class="letterhead-rule"></div>
  <div class="letterhead-footer">
    14 Larkwood Lane Syracuse, NY13099 &nbsp;|&nbsp; P : 315-555-0142 &nbsp;|&nbsp; F : 315-555-0178 &nbsp;|&nbsp; W : www.birchharborny.example
  </div>
  <div class="bottom-band"></div>
</section>

<section class="piece card">
  <div class="brand">
    <div class="brand-square"></div>
    <div class="brand-name">BirchHarbor</div>
  </div>
  <div class="card-panel">
    <div class="card-name">Kevin Rasble</div>
    <div class="card-role">President</div>
    <div class="card-block">14 Larkwood Lane<br>Syracuse, NY13099</div>
    <div class="card-block">P : 315-555-0142<br>F : 315-555-0178<br>info@birchharborny.example<br>www.birchharborny.example</div>
  </div>
</section>

</body>
</html>
```